Tova Meadows brand , chocolate packaging design

Tova Meadows

Products List

CANNABIS INFUSED CHOCOLATE BAR
(4 Flavor Chocolate Bar)
Original Milk chocolate Bar
Cookies N Cream Bar
Strawberry Cheesecake Bar
S’mores Bar

Information Front
-1000 MG THC Per package
-100mg THC per serving
-Made with Belgian Chocolate
-Made with Quality California Cannabis Extracts
-Net weight of bar 50grams
-California triangle warning symbol
-Flavor of chocolate bar

Information Back

-10 Servings per package
-100 mg serving size

-Directions
Wait 1-2 hours for full effect before consuming more.
-Very potent , Keep out of reach of children

-Store at 68-77° F
-Will melt in prolonged heat
-California government warning and ad41notice website

Ingredient list

Milk chocolate Bar
MILK CHOCOLATE (SUGAR, COCOA BUTTER , UNSWEETENED CHOCOLATE, SUNFLOWER LECITHIN, VANILLA) , CANNABIS EXTRACT.
ALLERGENS-CONTAINS MILK

Strawberry Cheesecake
WHITE CHOCOLATE (SUGAR, COCOA BUTTER, WHOLE MILK POWDER ,SOY LECITHIN, NATURAL VANILLA FLAVOR) STRAWBERRY POWDER , STRAWBERRY EXTRACT , NATURAL FLAVORS, CANNABIS EXTRACT.

Cookies n cream
WHITE CHOCOLATE (SUGAR, COCOA BUTTER, WHOLE MILK POWDER ,SOY LECITHIN, NATURAL VANILLA FLAVOR) 9
KRUNDELS (SUGAR, WHITE RICE FLOUR, TAPIOCA STARCH, PALM OIL, CANOLA OIL, WHOLE OAT FLOUR, CORN STARCH , COCOA (PROCESSED WITH ALKALI), INVERT SUGAR, SOY LECITHIN, BAKING SODA, SALT, XANTHAM GUM , CHOCOLATE, ARTIFICIAL FLAVOR, CANNABIS EXTRACT

S’mores
MILK CHOCOLATE (SUGAR, COCOA BUTTER, MILK, UNSWEETENED CHOCOLATE ,SUNFLOWER LECITHIN, VANILLA), MARSHMALLOW (SUGAR ,CORN SYRUP , MODIFIED STARCH, GELATIN, SODIUM HEXAMETAPHOSPHATE, ARTIFICIAL FLAVOR , NATURAL FLAVOR , ARTIFICIAL COLO (BLUE 1)), GRAHAM CRACKER (CORN STARCH, BROWN SUGAR , CORN FLOUR, PALM FAT , SOY FLOUR , SOY BRAN, HONEY, MODIFIED TAPIOCA STARCH, AMMONIUM BICARBONATE, BAKING SODA, SALT, CARAMELIZED SUGAR) NATURAL FLAVOR, CANNABIS EXTRACT.

Looking for simple clean modern design , chocolate bar can be like marivel of like the Brisbury one with images on it , and gummy is a mylar bag I really like the Brisbury style , I can provide dieline etc thank you !

Target Market(s)

Young adults

Industry/Entity Type

Cannabis , Delta 8 , CBD

Requirements
Must have
• Chocolate bar is box , dielines Included with images
Nice to have
• Simple clean , elegant and modern design , like the marivel and Brisbury brands , white logo preferred

```html
<!DOCTYPE html>
<html lang="en">
<head>
<meta charset="utf-8">
<title>Tova Meadows – Cannabis Infused Chocolate Bars</title>
<link href="https://fonts.googleapis.com/css2?family=Questrial&family=Open+Sans:wght@400;600&display=swap" rel="stylesheet">
<style>
  :root {
    --bg-top: #fe7a92;
    --bg-bottom: #d4b3c8;
    --teal: #2e6364;
    --teal-light: #3b7777;
    --cream: #fbf3ec;
    --white: #ffffff;
    --ink: #1d1d1d;
    --blue: #1b7bb7;
    --red: #8f1022;
    --purple: #7742a8;
    --brown: #7b3915;
  }
  * { box-sizing: border-box; margin: 0; padding: 0; }
  html, body { width: 1200px; height: 900px; overflow: hidden; }
  body {
    position: relative;
    background: linear-gradient(180deg, var(--bg-top) 0%, var(--bg-top) 12%, var(--bg-bottom) 100%);
    font-family: "Questrial", sans-serif;
    color: var(--cream);
  }

  .pack {
    position: absolute;
    top: 133px;
    background: var(--teal);
    box-shadow: 0 10px 22px rgba(60, 20, 40, 0.35);
    overflow: hidden;
  }
  .pack--short { width: 260px; height: 594px; }
  .pack--tall  { width: 277px; height: 634px; }

  .pack__leaves {
    position: absolute; left: 0; top: 0; width: 100%; height: 290px;
    background: radial-gradient(ellipse 80% 70% at 10% 5%, var(--teal-light) 0%, rgba(59,119,119,0.4) 50%, rgba(46,99,100,0) 100%);
  }

  .brand-frame {
    position: absolute;
    left: 28px; top: 212px; width: 207px; height: 99px;
    border: 1.5px solid var(--cream);
    border-radius: 6px;
    text-align: center;
  }
  .pack--tall .brand-frame { left: 29px; top: 227px; width: 221px; height: 105px; }

  .brand-frame__name {
    position: absolute; left: 50%; top: -16px;
    transform: translateX(-50%);
    padding: 0 8px;
    background: var(--teal);
    font-size: 25px; line-height: 30px; letter-spacing: 1px;
    white-space: nowrap; color: var(--cream);
  }
  .brand-frame__body {
    position: absolute; left: 0; right: 0; top: 37px;
    display: flex; flex-direction: column; align-items: center;
  }
  .brand-frame__rule { width: 67%; height: 1px; background: var(--cream); margin-bottom: 5px; }
  .brand-frame__kicker { font-family: "Open Sans", sans-serif; font-size: 12px; line-height: 14px; }
  .brand-frame__flavor { font-family: "Open Sans", sans-serif; font-size: 18px; line-height: 22px; letter-spacing: 0.3px; white-space: nowrap; }
  .brand-frame__note { font-family: "Open Sans", sans-serif; font-size: 7px; line-height: 10px; }
  .pack--tall .brand-frame__flavor { font-size: 17px; }

  .label {
    position: absolute;
    left: 16px; top: 400px; width: 229px; height: 194px;
    background: var(--accent);
    border: 1px solid rgba(255,255,255,0.6);
    border-bottom: none;
    overflow: hidden;
  }
  .pack--tall .label { left: 17px; top: 428px; width: 243px; height: 206px; }

  .thc-box {
    position: absolute; left: 45px; top: 23px; width: 159px; height: 58px;
    border: 1.5px solid var(--cream); border-radius: 4px;
    display: flex; align-items: stretch;
  }
  .pack--tall .thc-box { left: 47px; top: 23px; width: 170px; height: 62px; }
  .thc-box__tag {
    width: 36px; border-right: 1.5px solid var(--cream);
    display: flex; align-items: center; justify-content: center;
  }
  .thc-box__tag span {
    display: block; transform: rotate(-90deg);
    font-size: 25px; letter-spacing: 1px; line-height: 1;
  }
  .thc-box__dose {
    flex: 1; display: flex; flex-direction: column; justify-content: center;
    padding-left: 6px; font-size: 10.5px; line-height: 12.5px; white-space: nowrap;
  }
  .label__note {
    position: absolute; left: 0; right: 0; top: 84px;
    text-align: center; font-family: "Open Sans", sans-serif; font-size: 7px;
  }
  .pack--tall .label__note { top: 91px; }

  .label__photo {
    position: absolute; left: 0; right: 0; bottom: 0; height: 80px;
    background: linear-gradient(180deg, rgba(255,255,255,0) 0%, rgba(255,255,255,0.85) 45%, var(--photo) 80%, var(--white) 100%);
  }
  .pack--tall .label__photo { height: 78px; }

  .label__warning { position: absolute; left: 6px; bottom: 4px; width: 26px; height: 24px; }
  .label__weight {
    position: absolute; right: 12px; bottom: 7px;
    font-family: "Open Sans", sans-serif; font-size: 7.5px; color: var(--ink);
  }

  .pack--cookies { left: 25px;  --accent: var(--blue);   --photo: #55534f; }
  .pack--berry   { left: 314px; --accent: var(--red);    --photo: #e06a78; }
  .pack--milk    { left: 612px; --accent: var(--purple); --photo: #6b3a26; }
  .pack--smores  { left: 910px; --accent: var(--brown);  --photo: #8a5a34; }
</style>
</head>
<body>

<section class="pack pack--short pack--cookies">
  <div class="pack__leaves" role="img" aria-label="Faint cannabis leaf pattern"></div>
  <div class="brand-frame">
    <div class="brand-frame__name">TOVA MEADOWS</div>
    <div class="brand-frame__body">
      <div class="brand-frame__rule"></div>
      <p class="brand-frame__kicker">CANNABIS INFUSED</p>
      <p class="brand-frame__flavor">COOKIES N CREAM</p>
      <p class="brand-frame__note">Made with Quality California Cannabis Extracts</p>
    </div>
  </div>
  <div class="label">
    <div class="thc-box">
      <div class="thc-box__tag"><span>THC</span></div>
      <div class="thc-box__dose"><span>1000 MG Per package</span><span>100MG Per serving</span></div>
    </div>
    <p class="label__note">Ade with Belgian Chocolate</p>
    <div class="label__photo" role="img" aria-label="Cookies and ice cream in a milk splash"></div>
    <svg class="label__warning" viewBox="0 0 26 24" aria-hidden="true"><path d="M13 2 L24 22 H2 Z" fill="none" stroke="#1d1d1d" stroke-width="2" stroke-linejoin="round"/></svg>
    <p class="label__weight">NET WEIGHT 50G</p>
  </div>
</section>

<section class="pack pack--tall pack--berry">
  <div class="pack__leaves" role="img" aria-label="Faint cannabis leaf pattern"></div>
  <div class="brand-frame">
    <div class="brand-frame__name">TOVA MEADOWS</div>
    <div class="brand-frame__body">
      <div class="brand-frame__rule"></div>
      <p class="brand-frame__kicker">CANNABIS INFUSED</p>
      <p class="brand-frame__flavor">STRAWBERRY CHEESECAKE</p>
      <p class="brand-frame__note">Made with Quality California Cannabis Extracts</p>
    </div>
  </div>
  <div class="label">
    <div class="thc-box">
      <div class="thc-box__tag"><span>THC</span></div>
      <div class="thc-box__dose"><span>1000 MG Per package</span><span>100MG Per serving</span></div>
    </div>
    <p class="label__note">Ade with Belgian Chocolate</p>
    <div class="label__photo" role="img" aria-label="Strawberries in a pink milk splash"></div>
    <svg class="label__warning" viewBox="0 0 26 24" aria-hidden="true"><path d="M13 2 L24 22 H2 Z" fill="none" stroke="#1d1d1d" stroke-width="2" stroke-linejoin="round"/></svg>
    <p class="label__weight">NET WEIGHT 50G</p>
  </div>
</section>

<section class="pack pack--tall pack--milk">
  <div class="pack__leaves" role="img" aria-label="Faint cannabis leaf pattern"></div>
  <div class="brand-frame">
    <div class="brand-frame__name">TOVA MEADOWS</div>
    <div class="brand-frame__body">
      <div class="brand-frame__rule"></div>
      <p class="brand-frame__kicker">CANNABIS INFUSED</p>
      <p class="brand-frame__flavor">MILK CHOCOLATE</p>
      <p class="brand-frame__note">Made with Quality California Cannabis Extracts</p>
    </div>
  </div>
  <div class="label">
    <div class="thc-box">
      <div class="thc-box__tag"><span>THC</span></div>
      <div class="thc-box__dose"><span>1000 MG Per package</span><span>100MG Per serving</span></div>
    </div>
    <p class="label__note">Ade with Belgian Chocolate</p>
    <div class="label__photo" role="img" aria-label="Milk and chocolate swirling splash"></div>
    <svg class="label__warning" viewBox="0 0 26 24" aria-hidden="true"><path d="M13 2 L24 22 H2 Z" fill="none" stroke="#1d1d1d" stroke-width="2" stroke-linejoin="round"/></svg>
    <p class="label__weight">NET WEIGHT 50G</p>
  </div>
</section>

<section class="pack pack--short pack--smores">
  <div class="pack__leaves" role="img" aria-label="Faint cannabis leaf pattern"></div>
  <div class="brand-frame">
    <div class="brand-frame__name">TOVA MEADOWS</div>
    <div class="brand-frame__body">
      <div class="brand-frame__rule"></div>
      <p class="brand-frame__kicker">CANNABIS INFUSED</p>
      <p class="brand-frame__flavor">S’MORES</p>
      <p class="brand-frame__note">Made with Quality California Cannabis Extracts</p>
    </div>
  </div>
  <div class="label">
    <div class="thc-box">
      <div class="thc-box__tag"><span>THC</span></div>
      <div class="thc-box__dose"><span>1000 MG Per package</span><span>100MG Per serving</span></div>
    </div>
    <p class="label__note">Ade with Belgian Chocolate</p>
    <div class="label__photo" role="img" aria-label="S’mores with marshmallow and chocolate in a milk splash"></div>
    <svg class="label__warning" viewBox="0 0 26 24" aria-hidden="true"><path d="M13 2 L24 22 H2 Z" fill="none" stroke="#1d1d1d" stroke-width="2" stroke-linejoin="round"/></svg>
    <p class="label__weight">NET WEIGHT 50G</p>
  </div>
</section>

</body>
</html>
```